Create a book cover for a "Rollercoaster Log Book"

Hi,
I require a "Roller Coaster Log Book" book cover. It should be 7"x10" size and be created using vector graphics. You may create the graphics yourself or download them from vector websites. Fonts and graphics used on cover MUST have commercial licence. Please create something that's unique, lively and stands out. I require both the front and back covers (back cover can be simple). I will attach a book cover template below. If I like your cover design, I may hire you for future projects.

You’ll find some examples of roller coaster log books by searching on Quelbrix.com

Things I require:
1. Completed book cover file in source and PDF formats
2. Links to graphics you downloaded (if you downloaded). This is after winner is chosen.

Thank you

```html
<!DOCTYPE html>
<html lang="en">
<head>
<meta charset="utf-8">
<title>Roller Coaster Log Book – Cover</title>
<link rel="stylesheet" href="https://fonts.googleapis.com/css2?family=Archivo+Black&family=Poppins:wght@600&display=swap">
<style>
  :root {
    --stage: #e6e9ec;
    --paper: #ffffff;
    --navy: #1d2a5c;
    --green: #3f9b2f;
    --sky-top: #b9daf2;
    --sky-mid: #e3f1fb;
    --grass: #7dc242;
    --steel-light: #eef2f5;
    --steel: #c3ccd5;
    --track: #d9894a;
  }
  * { box-sizing: border-box; margin: 0; padding: 0; }
  html, body {
    width: 1200px;
    height: 848px;
    overflow: hidden;
    background: var(--stage);
  }
  .cover {
    position: absolute;
    left: 317px;
    top: 20px;
    width: 566px;
    height: 808px;
    background: var(--paper);
    overflow: hidden;
  }
  .top-rule {
    position: absolute;
    left: 0;
    top: 0;
    width: 100%;
    height: 10px;
    background: var(--navy);
  }
  .corner-block {
    position: absolute;
    left: 0;
    top: 0;
    width: 42px;
    height: 62px;
    background: var(--green);
  }
  .edition-tag {
    position: absolute;
    left: 0;
    top: 62px;
    width: 42px;
    height: 62px;
    background: var(--navy);
    display: flex;
    align-items: center;
    justify-content: center;
  }
  .edition-tag span {
    display: block;
    transform: rotate(-90deg);
    white-space: nowrap;
    color: var(--paper);
    font-family: "Poppins", sans-serif;
    font-size: 11px;
    line-height: 1.05;
    text-align: center;
  }
  .title {
    position: absolute;
    left: 62px;
    top: 30px;
    width: 480px;
    text-align: right;
  }
  .title-main {
    display: block;
    font-family: "Archivo Black", sans-serif;
    font-size: 84px;
    line-height: 0.95;
    color: var(--navy);
    letter-spacing: -1px;
  }
  .title-sub {
    display: block;
    font-family: "Poppins", sans-serif;
    font-weight: 600;
    font-size: 62px;
    line-height: 1;
    color: var(--green);
    margin-top: -2px;
    padding-right: 30px;
  }
  .sky {
    position: absolute;
    left: 0;
    top: 200px;
    width: 100%;
    height: 608px;
    background: linear-gradient(180deg, var(--sky-top) 0%, var(--sky-mid) 55%, #f2f8fc 86%, var(--grass) 90%, var(--green) 100%);
  }
  .coaster-art {
    position: absolute;
    left: 24px;
    top: 236px;
    width: 330px;
    height: 520px;
    border-radius: 160px 160px 12px 12px;
    background: linear-gradient(160deg, var(--steel-light) 0%, var(--steel) 70%, var(--track) 100%);
    opacity: 0.9;
  }
  .log-label {
    position: absolute;
    left: 372px;
    top: 572px;
    font-family: "Archivo Black", sans-serif;
    font-size: 40px;
    line-height: 1.05;
    color: var(--navy);
    transform: rotate(8deg);
    text-align: left;
  }
</style>
</head>
<body>
  <main class="cover">
    <div class="top-rule"></div>
    <div class="corner-block"></div>
    <div class="edition-tag"><span>edition<br>2022</span></div>

    <h1 class="title">
      <span class="title-main">ROLLER</span>
      <span class="title-sub">coaster</span>
    </h1>

    <div class="sky" aria-hidden="true"></div>
    <div class="coaster-art" role="img" aria-label="Illustration of a steel roller coaster loop with riders, floating balloons and pine trees under a blue sky with clouds"></div>

    <p class="log-label">LOG<br>BOOK</p>
  </main>
</body>
</html>
```